Spice Mix Label Bottle Branding - Health and Weight Loss Mixes

The company is called ZestRow Spice Mix's. We've created 5 spice mixes using ingredients that promote health and weight loss. We already have a logo but now we need labels for our bottles. We would like to see designs that have the feel of health supplements (see attached examples)

We would like a different colour featured with each of our flavours.

Our flavours are:
-Golden Chai (Yellow)
-Mild Curry (Orange)
-Coffee Rub (brown)
-Garlic Oregano (Green)
-Taco (Blue)

Thank you!

Target Market(s)

Ages 22-35. Men and Female. Trendy, Hipster.

Industry/Entity Type

Food Production

Font styles to use
Sans Serif

Colors
f37122
0655a3
0692cd
9bcb3c
fbee3f

Requirements
Must have
• A different featured colour for each flavour.
• The ZestRow Spices Logo (attached)
• The slogan: "Weight Loss Ingredients"
• -Golden Chai (Yellow)
• -Mild Curry (Orange)
• -Coffee Rub (brown)
• -Garlic Oregano (Green)
• -Taco (Blue)
• Text Files attached.
Nice to have
• A black label with a featured colour for each of the spice mice flavours.
• 'No Salt added'

```html
<!DOCTYPE html>
<html lang="en">
<head>
<meta charset="utf-8">
<title>ZestRow Spices — Bottle Labels</title>
<link href="https://fonts.googleapis.com/css2?family=Bebas+Neue&family=Oswald:wght@600&family=Open+Sans:ital,wght@0,700;1,400&display=swap" rel="stylesheet">
<style>
  :root {
    --sheet-bg: #e4e5e7;
    --label-black: #121212;
    --label-black-soft: #1d1d1d;
    --panel-white: #ffffff;
    --ink-dark: #161616;
    --text-white: #ffffff;
    --chai-yellow: #d9a22a;
    --coffee-brown: #a0652e;
    --garlic-green: #9bb83c;
    --taco-blue: #2f6aa3;
    --curry-orange: #f0622a;
  }
  * { box-sizing: border-box; margin: 0; padding: 0; }
  html, body { width: 1200px; height: 2452px; overflow: hidden; }
  body {
    position: relative;
    background: var(--sheet-bg);
    font-family: "Open Sans", Arial, sans-serif;
  }
  .hero {
    position: absolute; left: 0; top: 0; width: 1200px; height: 777px;
    background: linear-gradient(180deg, #d6d7da 0%, #f1f1f2 70%, #e8e8ea 100%);
  }
  .hero .label {
    top: 221px; left: 120px;
    transform: scale(0.8); transform-origin: top left;
    width: 1200px;
  }
  .label {
    position: absolute; left: 0; width: 1200px; height: 335px;
    background: radial-gradient(ellipse at 50% 40%, var(--label-black-soft) 0%, var(--label-black) 75%);
    overflow: hidden;
  }
  .label--chai   { top: 777px;  --accent: var(--chai-yellow); }
  .label--coffee { top: 1115px; --accent: var(--coffee-brown); }
  .label--garlic { top: 1453px; --accent: var(--garlic-green); }
  .label--taco   { top: 1792px; --accent: var(--taco-blue); }
  .label--curry  { top: 2129px; --accent: var(--curry-orange); }
  .hero .label--curry { top: 221px; }

  .brand-panel { position: absolute; left: 400px; top: 0; width: 400px; height: 182px; }
  .brand-panel svg { position: absolute; inset: 0; }
  .brand-name {
    position: absolute; left: 0; right: 0; top: 48px;
    display: flex; align-items: center; justify-content: center; gap: 12px;
    font-family: "Oswald", Arial, sans-serif; font-weight: 600;
    font-size: 46px; color: var(--ink-dark); letter-spacing: 0.5px;
  }
  .brand-dot { width: 18px; height: 18px; border-radius: 50%; background: var(--accent); }

  .blurb {
    position: absolute; top: 66px; width: 270px;
    color: var(--text-white); font-style: italic;
    font-size: 12.5px; line-height: 18.5px; text-align: center;
  }
  .blurb--left { left: 62px; }
  .blurb--right { right: 62px; }

  .flavour {
    position: absolute; left: 0; right: 0; top: 188px;
    text-align: center; font-family: "Bebas Neue", Arial, sans-serif;
    font-size: 62px; line-height: 62px; color: var(--text-white); letter-spacing: 1px;
    text-shadow: 3px 3px 0 var(--accent);
  }
  .slogan-band {
    position: absolute; left: 0; right: 0; top: 260px; height: 32px;
    background: var(--accent);
    display: flex; align-items: center; justify-content: center;
    font-weight: 700; font-size: 14px; letter-spacing: 3px;
    color: var(--ink-dark); text-transform: uppercase;
  }
  .net-weight {
    position: absolute; left: 0; right: 0; top: 302px;
    text-align: center; color: var(--text-white);
    font-weight: 700; font-size: 13px; letter-spacing: 1px;
  }
</style>
</head>
<body>

<section class="hero">
  <article class="label label--curry">
    <div class="brand-panel">
      <svg viewBox="0 0 400 182" width="400" height="182"><polygon points="0,0 400,0 400,138 200,182 0,138" fill="#fff"/></svg>
      <div class="brand-name"><span class="brand-dot"></span>ZestRow Spices</div>
    </div>
    <p class="blurb blurb--left">Lorem Ipsum is simply dummy text of the printing and typesetting industry. Lorem Ipsum has been the industry's standard dummy text ever since the 1500s, when an unknown printer took a galley of type and scrambled it to make a type specimen book. It has survived not only five centuries.</p>
    <p class="blurb blurb--right">Lorem Ipsum is simply dummy text of the printing and typesetting industry. Lorem Ipsum has been the industry's standard dummy text ever since the 1500s, when an unknown printer took a galley of type and scrambled it to make a type specimen book. It has survived not only five centuries.</p>
    <h2 class="flavour">Mild Curry</h2>
    <div class="slogan-band">Weight Loss Ingredients</div>
    <p class="net-weight">NT. WT. 100 G.</p>
  </article>
</section>

<article class="label label--chai">
  <div class="brand-panel">
    <svg viewBox="0 0 400 182" width="400" height="182"><polygon points="0,0 400,0 400,138 200,182 0,138" fill="#fff"/></svg>
    <div class="brand-name"><span class="brand-dot"></span>ZestRow Spices</div>
  </div>
  <p class="blurb blurb--left">Lorem Ipsum is simply dummy text of the printing and typesetting industry. Lorem Ipsum has been the industry's standard dummy text ever since the 1500s, when an unknown printer took a galley of type and scrambled it to make a type specimen book. It has survived not only five centuries.</p>
  <p class="blurb blurb--right">Lorem Ipsum is simply dummy text of the printing and typesetting industry. Lorem Ipsum has been the industry's standard dummy text ever since the 1500s, when an unknown printer took a galley of type and scrambled it to make a type specimen book. It has survived not only five centuries.</p>
  <h2 class="flavour">Golden Chai</h2>
  <div class="slogan-band">Weight Loss Ingredients</div>
  <p class="net-weight">NT. WT. 100 G.</p>
</article>

<article class="label label--coffee">
  <div class="brand-panel">
    <svg viewBox="0 0 400 182" width="400" height="182"><polygon points="0,0 400,0 400,138 200,182 0,138" fill="#fff"/></svg>
    <div class="brand-name"><span class="brand-dot"></span>ZestRow Spices</div>
  </div>
  <p class="blurb blurb--left">Lorem Ipsum is simply dummy text of the printing and typesetting industry. Lorem Ipsum has been the industry's standard dummy text ever since the 1500s, when an unknown printer took a galley of type and scrambled it to make a type specimen book. It has survived not only five centuries.</p>
  <p class="blurb blurb--right">Lorem Ipsum is simply dummy text of the printing and typesetting industry. Lorem Ipsum has been the industry's standard dummy text ever since the 1500s, when an unknown printer took a galley of type and scrambled it to make a type specimen book. It has survived not only five centuries.</p>
  <h2 class="flavour">Coffee Rub</h2>
  <div class="slogan-band">Weight Loss Ingredients</div>
  <p class="net-weight">NT. WT. 100 G.</p>
</article>

<article class="label label--garlic">
  <div class="brand-panel">
    <svg viewBox="0 0 400 182" width="400" height="182"><polygon points="0,0 400,0 400,138 200,182 0,138" fill="#fff"/></svg>
    <div class="brand-name"><span class="brand-dot"></span>ZestRow Spices</div>
  </div>
  <p class="blurb blurb--left">Lorem Ipsum is simply dummy text of the printing and typesetting industry. Lorem Ipsum has been the industry's standard dummy text ever since the 1500s, when an unknown printer took a galley of type and scrambled it to make a type specimen book. It has survived not only five centuries.</p>
  <p class="blurb blurb--right">Lorem Ipsum is simply dummy text of the printing and typesetting industry. Lorem Ipsum has been the industry's standard dummy text ever since the 1500s, when an unknown printer took a galley of type and scrambled it to make a type specimen book. It has survived not only five centuries.</p>
  <h2 class="flavour">Garlic Oregano</h2>
  <div class="slogan-band">Weight Loss Ingredients</div>
  <p class="net-weight">NT. WT. 100 G.</p>
</article>

<article class="label label--taco">
  <div class="brand-panel">
    <svg viewBox="0 0 400 182" width="400" height="182"><polygon points="0,0 400,0 400,138 200,182 0,138" fill="#fff"/></svg>
    <div class="brand-name"><span class="brand-dot"></span>ZestRow Spices</div>
  </div>
  <p class="blurb blurb--left">Lorem Ipsum is simply dummy text of the printing and typesetting industry. Lorem Ipsum has been the industry's standard dummy text ever since the 1500s, when an unknown printer took a galley of type and scrambled it to make a type specimen book. It has survived not only five centuries.</p>
  <p class="blurb blurb--right">Lorem Ipsum is simply dummy text of the printing and typesetting industry. Lorem Ipsum has been the industry's standard dummy text ever since the 1500s, when an unknown printer took a galley of type and scrambled it to make a type specimen book. It has survived not only five centuries.</p>
  <h2 class="flavour">Taco</h2>
  <div class="slogan-band">Weight Loss Ingredients</div>
  <p class="net-weight">NT. WT. 100 G.</p>
</article>

<article class="label label--curry">
  <div class="brand-panel">
    <svg viewBox="0 0 400 182" width="400" height="182"><polygon points="0,0 400,0 400,138 200,182 0,138" fill="#fff"/></svg>
    <div class="brand-name"><span class="brand-dot"></span>ZestRow Spices</div>
  </div>
  <p class="blurb blurb--left">Lorem Ipsum is simply dummy text of the printing and typesetting industry. Lorem Ipsum has been the industry's standard dummy text ever since the 1500s, when an unknown printer took a galley of type and scrambled it to make a type specimen book. It has survived not only five centuries.</p>
  <p class="blurb blurb--right">Lorem Ipsum is simply dummy text of the printing and typesetting industry. Lorem Ipsum has been the industry's standard dummy text ever since the 1500s, when an unknown printer took a galley of type and scrambled it to make a type specimen book. It has survived not only five centuries.</p>
  <h2 class="flavour">Mild Curry</h2>
  <div class="slogan-band">Weight Loss Ingredients</div>
  <p class="net-weight">NT. WT. 100 G.</p>
</article>

</body>
</html>
```